Update, redesign www.quorvane.net. Put it on WordPress and migrate to new host site

My current website is www.quorvane.net. The text content is ok but the site look and feel is several years old and does not project a sense of innovation. I am looking for a more modern exciting look. It needs to be built on word press and I need help in in putting it with a new hosting service.

Target Market(s)

Established organizations

Industry/Entity Type

Business Consultant

Number of Pages Required

1 page

Font styles to use
Sans Serif

Colors

Designer to choose colors to be used in the design.

Requirements
Must have
• Simple. Easy to read and navigate
Nice to have
• Innovation, creativity especially the leadership of innovation. Reading the current text on www.quorvane.net should help you with ideas
Should not have
• Difficulty in me managing or adding content after it is built

```html
<!DOCTYPE html>
<html lang="en">
<head>
<meta charset="utf-8">
<title>Quorvane – Innovation at Work</title>
<link rel="stylesheet" href="https://fonts.googleapis.com/css2?family=Raleway:wght@400;500;600;700;800&display=swap">
<style>
:root{
  --red:#ee2f3b;
  --red-dark:#c81f2a;
  --ink:#1b1b1b;
  --text:#444;
  --muted:#777;
  --black:#000;
  --white:#fff;
  --line:#d9d9d9;
  --strip:#f4f4f4;
  --soft:#fafafa;
  --logo-grey:#b9b9b9;
}
*{box-sizing:border-box;margin:0;padding:0}
html,body{width:1200px;height:2332px;overflow:hidden;background:var(--white)}
body{position:relative;font-family:"Raleway",Arial,sans-serif;color:var(--ink)}
.abs{position:absolute}

/* header */
.site-header{left:0;top:0;width:1200px;height:66px;background:var(--white);border-bottom:1px solid #e6e6e6}
.brand{left:117px;top:12px;display:flex;align-items:baseline;gap:16px}
.brand-name{font-size:31px;font-weight:700;color:var(--red);letter-spacing:-.5px}
.brand-tag{font-size:13px;color:var(--muted)}
.main-nav a{position:absolute;top:25px;font-size:11px;color:var(--ink);text-decoration:none;transform:translateX(-50%);white-space:nowrap}
.btn-touch{left:980px;top:17px;width:113px;height:33px;background:var(--red);color:var(--white);font-size:11px;font-weight:600;display:flex;align-items:center;justify-content:center;border-radius:2px}

/* hero */
.hero{left:0;top:66px;width:1200px;height:491px;background:var(--black)}
.hero-eyebrow{left:120px;top:186px;font-size:28px;letter-spacing:3px;color:var(--red);font-weight:500}
.hero-title{left:120px;top:222px;font-size:40px;font-weight:800;color:var(--white)}
.hero-rule{left:126px;top:302px;width:48px;height:3px;background:var(--white)}
.hero-lead{left:126px;top:334px;width:430px;font-size:19px;line-height:28px;color:var(--white)}
.hero-visual{left:684px;top:66px;width:436px;height:491px;background:radial-gradient(ellipse 38% 42% at 50% 38%,#7a1b16 0%,#3a0d0b 45%,#000 80%)}

/* client strip */
.clients{left:0;top:560px;width:1200px;height:82px;background:var(--strip);display:flex;align-items:center;justify-content:space-around;padding:0 20px}
.client-mark{background:var(--logo-grey);opacity:.7}

/* services */
.section-title{left:0;width:1200px;text-align:center;font-size:24px;font-weight:600;color:var(--ink)}
.section-title span{color:var(--red)}
.title-rule{left:583px;width:34px;height:3px;background:var(--ink)}
.service-card{background:var(--white);box-shadow:0 1px 6px rgba(0,0,0,.14);text-align:center;padding:0 18px}
.service-card svg{display:block;margin:0 auto}
.service-card h3{font-size:16px;font-weight:600;color:var(--ink);margin-top:14px}
.service-card p{font-size:10px;line-height:16px;color:var(--muted);margin-top:10px}
.service-card .more{display:block;font-size:10px;font-weight:600;color:var(--red);margin-top:10px}
.service-card.is-featured{background:var(--red);box-shadow:0 4px 14px rgba(0,0,0,.25)}
.service-card.is-featured h3,.service-card.is-featured p,.service-card.is-featured .more{color:var(--white)}

/* book promo */
.book-promo{left:0;top:1093px;width:1200px;height:481px;background:linear-gradient(180deg,#ececec 0%,#f3f3f3 60%,#dedede 100%)}
.book-cover{left:316px;top:1163px;width:247px;height:342px;background:linear-gradient(180deg,#e3262d 0%,#d9232a 62%,#0f2a33 62%,#0f2a33 84%,#d9232a 84%);box-shadow:0 4px 12px rgba(0,0,0,.25)}
.promo-title{left:625px;top:1224px;font-size:31px;font-weight:600;color:var(--ink)}
.promo-text{left:625px;top:1282px;width:450px;font-size:15px;line-height:25px;color:#666}
.btn-buy{left:623px;top:1388px;width:106px;height:28px;background:var(--red);color:var(--white);font-size:11px;font-weight:600;display:flex;align-items:center;justify-content:center;border-radius:2px}
.slider-next{left:1114px;top:1310px;width:46px;height:46px;border:1.5px solid var(--ink);border-radius:50%;display:flex;align-items:center;justify-content:center}

/* about */
.about-brand{left:160px;top:1676px;font-size:46px;font-weight:700;color:var(--red);letter-spacing:-.5px}
.about-text{left:445px;top:1650px;width:600px;font-size:15px;line-height:30px;color:#666}

/* contact */
.contact{left:0;top:1851px;width:1200px;height:481px;background:var(--soft);border-top:1px solid #ececec}
.contact-item{width:220px;text-align:center;font-size:12px;color:var(--ink);transform:translateX(-50%)}
.contact-item svg{display:block;margin:0 auto 10px}
.field{background:var(--white);border:1px solid var(--line);font-size:11px;color:var(--ink);padding:12px 18px}
.footer-rule{left:247px;width:695px;height:1px;background:#bbb}
.footer-nav a{position:absolute;top:2265px;font-size:9px;color:var(--ink);text-decoration:none;transform:translateX(-50%);white-space:nowrap}
.legal{left:0;top:2298px;width:1200px;text-align:center;font-size:8px;color:var(--ink)}
</style>
</head>
<body>

<header class="site-header abs">
  <div class="brand abs"><span class="brand-name">quorvane</span><span class="brand-tag">Innovation at Work</span></div>
  <nav class="main-nav">
    <a style="left:574px">About</a>
    <a style="left:690px">Thoughts Leadership</a>
    <a style="left:818px">Services</a>
    <a style="left:910px">Videos</a>
  </nav>
  <div class="btn-touch abs">Get In Touch</div>
</header>

<section class="hero abs">
</section>
<div class="hero-visual abs" role="img" aria-label="Photograph of a glowing red filament light bulb on black"></div>
<div class="hero-eyebrow abs">Innovation at Work</div>
<h1 class="hero-title abs">With Creative Team</h1>
<div class="hero-rule abs"></div>
<p class="hero-lead abs">Lorem ipsum dolor sit amet, consectetuer adip-iscing elit. Aenean commodo</p>

<div class="clients abs" aria-label="Client marks">
  <div class="client-mark" style="width:70px;height:24px"></div>
  <div class="client-mark" style="width:96px;height:18px"></div>
  <div class="client-mark" style="width:72px;height:28px;border-radius:50%"></div>
  <div class="client-mark" style="width:52px;height:52px;border-radius:50%"></div>
  <div class="client-mark" style="width:90px;height:18px"></div>
  <div class="client-mark" style="width:70px;height:24px"></div>
  <div class="client-mark" style="width:50px;height:24px"></div>
  <div class="client-mark" style="width:82px;height:18px"></div>
  <div class="client-mark" style="width:70px;height:22px"></div>
  <div class="client-mark" style="width:54px;height:30px"></div>
</div>

<h2 class="section-title abs" style="top:688px"><span>Quorvane</span> Services</h2>
<div class="title-rule abs" style="top:725px"></div>

<article class="service-card abs" style="left:107px;top:767px;width:226px;height:233px;padding-top:34px">
  <svg width="44" height="50" viewBox="0 0 44 50" fill="none" stroke="#ee2f3b" stroke-width="2"><circle cx="22" cy="18" r="14"/><circle cx="22" cy="18" r="9"/><path d="M22 12l2 4 4 .5-3 3 1 4-4-2-4 2 1-4-3-3 4-.5z"/><path d="M13 29l-5 15 7-3 4 6 3-9M31 29l5 15-7-3-4 6-3-9"/></svg>
  <h3>Consulting</h3>
  <p>When it comes to 'Quality', there is no middle ground. At Norvel Health Inc. there is no concession...</p>
  <span class="more">Read more</span>
</article>

<article class="service-card is-featured abs" style="left:334px;top:767px;width:272px;height:262px;padding-top:26px">
  <svg width="50" height="50" viewBox="0 0 50 50" fill="none" stroke="#fff" stroke-width="2"><path d="M40 12A20 20 0 1 0 45 25"/><path d="M40 4v8h-8"/><rect x="17" y="22" width="16" height="13" rx="1"/><path d="M20 22v-4a5 5 0 0 1 10 0v4"/><circle cx="25" cy="28" r="1.6"/></svg>
  <h3>Executive<br>Education</h3>
  <p>Information Security which is also known as data security is one of the main priorities or parameteu...</p>
  <span class="more">Read more</span>
</article>

<article class="service-card abs" style="left:606px;top:767px;width:229px;height:233px;padding-top:34px">
  <svg width="44" height="46" viewBox="0 0 44 46" fill="none" stroke="#ee2f3b" stroke-width="2"><rect x="8" y="12" width="20" height="30" rx="3"/><rect x="11" y="5" width="14" height="7"/><path d="M8 22h20M8 34h20"/><rect x="26" y="26" width="16" height="9" rx="4.5" transform="rotate(-35 34 30)"/></svg>
  <h3>Books</h3>
  <p>When it comes to 'Quality', there is no middle ground. At Norvel Health Inc. there is no concession...</p>
  <span class="more">Read more</span>
</article>

<article class="service-card abs" style="left:835px;top:767px;width:244px;height:233px;padding-top:30px">
  <svg width="40" height="48" viewBox="0 0 40 48" fill="none" stroke="#ee2f3b" stroke-width="2"><rect x="4" y="6" width="32" height="40" rx="3"/><rect x="13" y="2" width="14" height="8" rx="2"/><path d="M10 20l3 3 5-5M22 21h10M10 30l3 3 5-5M22 31h10M10 40h22"/></svg>
  <h3>Speaking</h3>
  <p>When it comes to 'Quality', there is no middle ground. At Norvel Health Inc. there is no concession...</p>
  <span class="more">Read more</span>
</article>

<section class="book-promo abs" role="img" aria-label="Photograph of a white desk with a potted plant, stacked books and glasses"></section>
<div class="book-cover abs" role="img" aria-label="Cover of the book Idea Leverage by Darren Holloway"></div>
<h2 class="promo-title abs">Order Idea Leverage</h2>
<p class="promo-text abs">Idea Leverage reveals 7 secret principles that can help any in-novator overcome the roadblocks and blockheads that they will inevitably meet on the path to creativity</p>
<div class="btn-buy abs">Buy Now</div>
<div class="slider-next abs"><svg width="14" height="14" viewBox="0 0 14 14" fill="none" stroke="#1b1b1b" stroke-width="2"><path d="M5 2l5 5-5 5"/></svg></div>

<div class="about-brand abs">quorvane</div>
<p class="about-text abs">Quorvane works with a broad range of national and global clients to utilize "Innovation at Work" to improve business results. We help individuals and organizations through the entire value chain of innovation from idea generation, implementation and value creation.</p>

<section class="contact abs"></section>
<h2 class="section-title abs" style="top:1902px"><span>Get in</span> Touch</h2>
<div class="title-rule abs" style="top:1940px"></div>

<div class="contact-item abs" style="left:407px;top:1972px">
  <svg width="18" height="26" viewBox="0 0 18 26"><path d="M9 0a9 9 0 0 0-9 9c0 7 9 17 9 17s9-10 9-17a9 9 0 0 0-9-9z" fill="#ee2f3b"/><circle cx="9" cy="9" r="3.5" fill="#fafafa"/></svg>
  2290 N Your full address
</div>
<div class="contact-item abs" style="left:597px;top:1980px">
  <svg width="22" height="17" viewBox="0 0 22 17"><rect width="22" height="17" fill="#ee2f3b"/><path d="M1 1l10 8 10-8" fill="none" stroke="#fafafa" stroke-width="1.6"/></svg>
  support@quorvane.net
</div>
<div class="contact-item abs" style="left:779px;top:1978px">
  <svg width="20" height="20" viewBox="0 0 24 24"><path d="M6.6 10.8a15.2 15.2 0 0 0 6.6 6.6l2.2-2.2a1 1 0 0 1 1-.25 11.4 11.4 0 0 0 3.6.6 1 1 0 0 1 1 1V20a1 1 0 0 1-1 1A17 17 0 0 1 3 4a1 1 0 0 1 1-1h3.5a1 1 0 0 1 1 1c0 1.25.2 2.45.6 3.6a1 1 0 0 1-.25 1z" fill="#ee2f3b"/></svg>
  (480) 555 - 0182
</div>

<div class="field abs" style="left:222px;top:2054px;width:366px;height:39px">Name</div>
<div class="field abs" style="left:222px;top:2115px;width:366px;height:39px">Email</div>
<div class="field abs" style="left:222px;top:2176px;width:366px;height:39px">Subject</div>
<div class="field abs" style="left:605px;top:2054px;width:367px;height:161px">Message</div>

<div class="footer-rule abs" style="top:2258px"></div>
<nav class="footer-nav">
  <a style="left:386px">About</a>
  <a style="left:482px">Thoughts Leadership</a>
  <a style="left:586px">Services</a>
  <a style="left:662px">Videos</a>
  <a style="left:767px">Get In Touch</a>
</nav>
<div class="footer-rule abs" style="top:2288px"></div>
<p class="legal abs">All rights reserved &nbsp;|&nbsp; Privacy Policy &nbsp;|&nbsp; Terms</p>

</body>
</html>
```